Infographics about Plumline Census

Hello, we are NexoraFlux, a leading Big Data and Data Science consultancy firm from The Netherlands. We are looking for an awesome infographic.

Introduction
In order to create a better understanding of the status of Big Data in our little country, together with the biggest Big Data trade show Quarry Summit Fair, we created the Plumline Census. This first national research on Big Data aims at providing insight in use of Big Data. The survey is built on five corner stones: Organization, Data, Technology, Skills and Process.

Design
We are looking for an insightful representation of the key-results of the survey, based on the five corner stones. It may also very well be multiple infographics in order to decrease the information density, but I'll leave that to you.

We are looking for a fresh, funky and attractive design, that is easily understood. Please use the colors (orange and blue) of the survey report. For more information see: http://www.nexoraflux.example/static/images/plumlinecensus/plumlinecensus-resultaten-web.pdf

```html
<!DOCTYPE html>
<html lang="en">
<head>
<meta charset="utf-8">
<title>Plumline Census 2015 – Infographic</title>
<link rel="stylesheet" href="https://fonts.googleapis.com/css2?family=Roboto:wght@300;400;700&display=swap">
<style>
  :root {
    --blue: #2f6eab;
    --blue-deep: #2a5f92;
    --blue-light: #3b87c9;
    --orange: #f08a24;
    --orange-soft: #f7ad63;
    --grey-bg: #e6e6e6;
    --white: #ffffff;
    --ink: #333333;
    --frame: #5a5f66;
    --dash: #ffffff;
  }
  * { box-sizing: border-box; margin: 0; padding: 0; }
  html, body { width: 1200px; height: 2517px; overflow: hidden; }
  body { font-family: "Roboto", Arial, sans-serif; font-weight: 300; color: var(--ink); background: var(--white); }
  .infographic { position: relative; width: 1200px; height: 2517px; overflow: hidden; }
  .section { position: absolute; left: 0; width: 1200px; }
  .abs { position: absolute; }
  .center { transform: translateX(-50%); text-align: center; white-space: nowrap; }

  /* Section 2 */
  .personalize { top: 0; height: 982px; background: var(--blue); color: var(--white); }
  .section-title { position: absolute; left: 0; width: 1200px; text-align: center; font-size: 33px; font-weight: 300; line-height: 1.2; }
  .personalize .section-title { top: 20px; }
  .stat-caption { font-size: 27px; line-height: 34px; color: var(--white); }
  .pct { position: absolute; width: 68px; height: 68px; border-radius: 50%; display: flex; align-items: center; justify-content: center; font-size: 23px; font-weight: 400; color: var(--white); transform: translate(-50%, -50%); }
  .pct--soft { background: var(--orange-soft); }
  .pct--strong { background: var(--orange); }
  .divider-v { position: absolute; width: 0; border-left: 3px dashed var(--dash); }
  .divider-h { position: absolute; height: 0; border-top: 3px dashed var(--dash); }
  .illustration { position: absolute; border-radius: 6px; }
  .illus-browser { background: linear-gradient(90deg, #dfe3e8 0 30%, #9aa3ad 30% 100%); }
  .illus-terminal { background: linear-gradient(180deg, #2f3640 0 85%, #d9dde2 85% 100%); }
  .illus-sheet { background: linear-gradient(90deg, #f2e2cf 0 50%, #cfd4da 50% 100%); border-radius: 2px; }
  .illus-dashboard { background: linear-gradient(180deg, #4a5058 0 12%, #f1f2f4 12% 100%); }

  /* Section 3 */
  .usage { top: 982px; height: 594px; background: var(--grey-bg); }
  .usage .section-title { top: 26px; color: var(--ink); }
  .group-label { font-size: 27px; font-weight: 700; color: var(--ink); }
  .bar-label { font-size: 26px; line-height: 36px; color: var(--ink); }
  .bar-value { font-size: 25px; color: var(--white); }
  .usage .divider-v { border-left-color: var(--ink); }

  /* Section 4 */
  .methods { top: 1576px; height: 575px; background: var(--white); }
  .methods .section-title { top: 28px; color: var(--ink); line-height: 56px; }
  .methods .stat-caption { color: var(--ink); }
  .methods .divider-v { border-left-color: var(--ink); }
  .monitor-frame { position: absolute; background: var(--frame); border-radius: 6px; }
  .monitor-screen { position: absolute; background: linear-gradient(90deg, #3a7dbd 0 100%); }
  .monitor-stand { position: absolute; background: #b9bec4; }

  /* Partners and footer */
  .band-orange { position: absolute; left: 0; width: 1200px; background: var(--orange); }
  .partners { top: 2187px; height: 167px; background: var(--white); }
  .partner { position: absolute; top: 58px; display: flex; align-items: center; gap: 14px; font-size: 40px; font-weight: 400; color: var(--blue-deep); white-space: nowrap; }
  .partner-mark { width: 38px; height: 38px; background: var(--blue-deep); }
  .footer { top: 2407px; height: 110px; background: var(--blue-light); }
  .footer-main { position: absolute; left: 0; top: 0; width: 718px; height: 110px; background: var(--blue-deep); color: var(--white); padding: 18px 0 0 43px; font-size: 26px; line-height: 46px; }
</style>
</head>
<body>
<main class="infographic">

  <section class="section personalize">
    <h2 class="section-title">2. To What Extent Do You Personalize Your Website?</h2>

    <!-- Not personalized -->
    <div class="illustration illus-browser" role="img" aria-label="Browser window icon" style="left:150px;top:204px;width:305px;height:160px"></div>
    <div class="divider-v" style="left:240px;top:132px;height:236px"></div>
    <div class="pct pct--soft" style="left:192px;top:168px">54%</div>
    <div class="pct pct--strong" style="left:292px;top:168px">46%</div>
    <p class="abs center stat-caption" style="left:300px;top:424px">46% does not personalize<br>its website</p>

    <!-- Manual -->
    <div class="illustration illus-terminal" role="img" aria-label="Laptop showing code" style="left:718px;top:216px;width:305px;height:167px"></div>
    <div class="divider-v" style="left:831px;top:132px;height:251px"></div>
    <div class="pct pct--soft" style="left:778px;top:168px">29%</div>
    <div class="pct pct--strong" style="left:884px;top:168px">71%</div>
    <p class="abs center stat-caption" style="left:879px;top:421px">29% does this manually</p>

    <!-- Historical data -->
    <div class="illustration illus-sheet" role="img" aria-label="Spreadsheet document icon" style="left:228px;top:539px;width:203px;height:263px"></div>
    <div class="divider-h" style="left:132px;top:757px;width:323px"></div>
    <div class="pct pct--soft" style="left:168px;top:702px">85%</div>
    <div class="pct pct--strong" style="left:168px;top:805px">15%</div>
    <p class="abs center stat-caption" style="left:300px;top:874px">15% personalizes based<br>on historical data</p>

    <!-- Real time -->
    <div class="illustration illus-dashboard" role="img" aria-label="Dashboard window with charts" style="left:762px;top:599px;width:273px;height:203px"></div>
    <div class="divider-v" style="left:790px;top:508px;height:294px"></div>
    <div class="pct pct--strong" style="left:742px;top:546px">11%</div>
    <div class="pct pct--soft" style="left:838px;top:546px">89%</div>
    <p class="abs center stat-caption" style="left:898px;top:836px">11% is able to personalize the<br>website in real-time based on<br>current visitor behavior</p>
  </section>

  <section class="section usage">
    <h2 class="section-title">3. What Do You Use Data For?</h2>
    <p class="abs center group-label" style="left:347px;top:110px">Bottom 3</p>
    <p class="abs center group-label" style="left:934px;top:110px">Top 3</p>

    <svg class="abs" style="left:0;top:0" width="1200" height="594" viewBox="0 0 1200 594" aria-hidden="true">
      <polygon fill="var(--blue)" points="103,563 103,503 271,503 271,443 431,443 431,383 599,383 599,323 766,323 766,259 934,259 934,208 1102,208 1102,563"/>
    </svg>
    <div class="divider-v" style="left:598px;top:108px;height:480px"></div>

    <p class="abs bar-label" style="left:120px;top:454px">HR</p>
    <p class="abs bar-value" style="left:168px;top:519px">3%</p>

    <p class="abs center bar-label" style="left:330px;top:370px">Finance and<br>Administration</p>
    <p class="abs bar-value" style="left:334px;top:459px">4%</p>

    <p class="abs center bar-label" style="left:500px;top:306px">Supply Chain<br>&amp; Logistics</p>
    <p class="abs bar-value" style="left:497px;top:399px">5%</p>

    <p class="abs center bar-label" style="left:682px;top:252px">Market<br>Analysis</p>
    <p class="abs bar-value" style="left:660px;top:340px">14%</p>

    <p class="abs center bar-label" style="left:850px;top:222px">Online</p>
    <p class="abs bar-value" style="left:830px;top:279px">16%</p>

    <p class="abs center bar-label" style="left:1018px;top:168px">Marketing</p>
    <p class="abs bar-value" style="left:997px;top:226px">19%</p>
  </section>

  <section class="section methods">
    <h2 class="section-title">4. Are Companies Planning to Use Advanced Methods, Like<br>Deep Learning, Artificial Intelligence and Predictive Models?</h2>

    <!-- Already using -->
    <div class="monitor-frame" style="left:216px;top:263px;width:359px;height:200px"></div>
    <div class="monitor-screen" role="img" aria-label="Monitor screen with a brain illustration" style="left:230px;top:277px;width:331px;height:172px"></div>
    <div class="monitor-stand" style="left:360px;top:463px;width:71px;height:24px"></div>
    <div class="divider-v" style="left:259px;top:172px;height:300px"></div>
    <div class="pct pct--strong" style="left:211px;top:208px">17%</div>
    <div class="pct pct--soft" style="left:311px;top:208px">83%</div>
    <p class="abs center stat-caption" style="left:395px;top:472px">17% is already using<br>these methods</p>

    <!-- Within 3 years -->
    <div class="monitor-frame" style="left:747px;top:263px;width:367px;height:200px"></div>
    <div class="monitor-screen" role="img" aria-label="Monitor screen with a brain illustration" style="left:761px;top:277px;width:339px;height:172px"></div>
    <div class="monitor-stand" style="left:895px;top:463px;width:71px;height:24px"></div>
    <div class="divider-v" style="left:833px;top:172px;height:300px"></div>
    <div class="pct pct--strong" style="left:786px;top:208px">40%</div>
    <div class="pct pct--soft" style="left:886px;top:208px">60%</div>
    <p class="abs center stat-caption" style="left:922px;top:472px">40% expects these methods to<br>be in production within 3 years</p>
  </section>

  <div class="band-orange" style="top:2151px;height:36px"></div>

  <section class="section partners">
    <div class="partner" style="left:60px"><span class="partner-mark"></span>NexoraFlux</div>
    <div class="partner" style="left:470px">Plumline Census</div>
    <div class="partner" style="left:800px">Quarry Summit Fair</div>
  </section>

  <div class="band-orange" style="top:2354px;height:53px"></div>

  <footer class="section footer">
    <div class="footer-main">
      <p>Plumline Census 2015, 186 participants</p>
      <p>www.plumlinecensus.example</p>
    </div>
  </footer>

</main>
</body>
</html>
```